Corporate Business Card

Very professional, Modern, Not to busy, include phone address email, website
(555) 555-0174, 61807 19th Street N, Alder Bend, OR 98517, marcus@kestrelbayholding.com, brelvanindustries.com

Target Market(s)

Manufacturing

Industry/Entity Type

Aero, machining, manufacturing, Off road racing

Contact Information for Business Card

Phone, address email, website

```html
<!DOCTYPE html>
<html lang="en">
<head>
<meta charset="UTF-8">
<title>Brelvan Industries – Business Card</title>
<link rel="stylesheet" href="https://fonts.googleapis.com/css2?family=Poppins:wght@400;600&display=swap">
<style>
  :root {
    --backdrop: #5a5c5e;
    --card-white: #ffffff;
    --card-black: #050505;
    --brand-navy: #173a7a;
    --brand-red: #d7262b;
    --ink-light: #f2f2f2;
    --shadow: rgba(0, 0, 0, 0.35);
  }
  * { box-sizing: border-box; margin: 0; padding: 0; }
  html, body {
    width: 1200px;
    height: 780px;
    overflow: hidden;
  }
  body {
    background: var(--backdrop);
    font-family: "Poppins", sans-serif;
    position: relative;
  }
  .card {
    position: absolute;
    top: 235px;
    width: 520px;
    height: 310px;
    border-radius: 24px;
    box-shadow: 0 14px 30px var(--shadow);
    overflow: hidden;
  }
  .card--front { left: 50px; background: var(--card-white); }
  .card--back { left: 630px; background: var(--card-black); color: var(--ink-light); }

  .brand-name {
    font-family: "Poppins", sans-serif;
    font-weight: 600;
    letter-spacing: 0.5px;
    white-space: nowrap;
  }
  .card--front .brand-name {
    position: absolute;
    left: 0; right: 0;
    top: 128px;
    text-align: center;
    font-size: 40px;
    color: var(--brand-navy);
  }
  .card--back .brand-name {
    position: absolute;
    left: 34px;
    top: 112px;
    font-size: 19px;
    color: var(--ink-light);
  }

  .divider {
    position: absolute;
    left: 228px;
    top: 70px;
    width: 2px;
    height: 120px;
    background: var(--brand-red);
  }
  .contact-list {
    position: absolute;
    left: 248px;
    top: 78px;
    list-style: none;
  }
  .contact-list li {
    display: flex;
    align-items: center;
    gap: 10px;
    font-size: 13px;
    line-height: 1;
    margin-bottom: 14px;
    white-space: nowrap;
  }
  .contact-list svg { width: 16px; height: 16px; flex: none; }

  .address {
    position: absolute;
    left: 100px;
    bottom: 52px;
    display: flex;
    align-items: center;
    gap: 12px;
    font-size: 14px;
    white-space: nowrap;
  }
  .address svg { width: 14px; height: 18px; flex: none; }
</style>
</head>
<body>

  <section class="card card--front" aria-label="Card front">
    <p class="brand-name">Brelvan Industries</p>
  </section>

  <section class="card card--back" aria-label="Card back">
    <p class="brand-name">Brelvan Industries</p>
    <span class="divider"></span>

    <ul class="contact-list">
      <li>
        <svg viewBox="0 0 24 24" aria-hidden="true"><path fill="#d7262b" d="M6.6 10.8a15.2 15.2 0 0 0 6.6 6.6l2.2-2.2a1 1 0 0 1 1-.25 11.4 11.4 0 0 0 3.6.57 1 1 0 0 1 1 1V20a1 1 0 0 1-1 1A17 17 0 0 1 3 4a1 1 0 0 1 1-1h3.5a1 1 0 0 1 1 1c0 1.25.2 2.45.57 3.57a1 1 0 0 1-.25 1z"/></svg>
        <span>(555) 555-0174</span>
      </li>
      <li>
        <svg viewBox="0 0 24 24" aria-hidden="true"><rect x="2" y="5" width="20" height="14" rx="1.5" fill="#d7262b"/><path d="M2.5 6l9.5 7 9.5-7" fill="none" stroke="#050505" stroke-width="1.6"/></svg>
        <span>marcus@kestrelbayholding.com</span>
      </li>
      <li>
        <svg viewBox="0 0 24 24" aria-hidden="true"><g fill="none" stroke="#d7262b" stroke-width="2"><circle cx="12" cy="12" r="9"/><ellipse cx="12" cy="12" rx="4" ry="9"/><path d="M3 12h18M5 7h14M5 17h14"/></g></svg>
        <span>brelvanindustries.com</span>
      </li>
    </ul>

    <p class="address">
      <svg viewBox="0 0 14 18" aria-hidden="true"><path fill="#f2f2f2" d="M7 0a7 7 0 0 0-7 7c0 5 7 11 7 11s7-6 7-11a7 7 0 0 0-7-7zm0 10a3 3 0 1 1 0-6 3 3 0 0 1 0 6z"/></svg>
      <span>61807 19th Street N, Alder Bend, OR 98517</span>
    </p>
  </section>

</body>
</html>
```